依頼概要
・株式会社森岡ホールディングスの社員募集のポスター作成して頂きたいです。

・詳細 黒を基調としたシンプルな感じなのですが、目にとまるインパクトさも必要。
『社員募集』は英語表記で『資格保有者優遇』(日本語OK)のワードは入れてほしい    です。
添付データの右上の会社ロゴの『MOKA』を背景に透かして入れてほしいです。

・ 重視する点 過去・現在までにデザインの経験のある方を希望致します。

・その他何かご不明な点がございましたら、お気軽にご質問下さい。
よろしくお願いいたします。
■ 選んだ理由

黒を基調のシンプルさの中にインパクトのあるデザインで気に入りました。

■ 提案者全員のお礼・コメント

この度は沢山の提案をして頂きありがとうございます。
また、機会があれば宜しくお願い致します。

```html
<!DOCTYPE html>
<html lang="ja">
<head>
<meta charset="utf-8">
<title>MOKA 社員募集ポスター</title>
<link href="https://fonts.googleapis.com/css2?family=Oswald:wght@300;500;600;700&family=Noto+Sans+JP:wght@400;500;700;900&display=swap" rel="stylesheet">
<style>
  :root {
    --ink: #0d0d0d;
    --panel: #1a1a1a;
    --cream: #efe6cf;
    --white: #ffffff;
    --ghost: rgba(255,255,255,0.05);
    --muted: #bdbdbd;
  }
  html, body { margin: 0; padding: 0; overflow: hidden; background: var(--ink); }
  .poster {
    position: relative; width: 846px; height: 1200px; overflow: hidden;
    background: radial-gradient(ellipse at 50% 35%, #262626 0%, var(--ink) 70%);
    font-family: "Noto Sans JP", sans-serif; color: var(--white);
  }
  .brand {
    position: absolute; left: 22px; top: 24px;
    display: flex; flex-direction: column; align-items: center; gap: 6px;
  }
  .brand-mark { width: 22px; height: 22px; background: var(--cream); }
  .brand-name { font-family: "Oswald", sans-serif; font-weight: 500; font-size: 15px; letter-spacing: 2px; color: var(--white); }
  .watermark {
    position: absolute; left: 50%; top: 250px; transform: translateX(-50%);
    font-family: "Oswald", sans-serif; font-weight: 700; font-size: 460px; line-height: 1;
    color: var(--ghost); letter-spacing: -6px; white-space: nowrap;
  }
  .lead {
    position: absolute; left: 82px; top: 128px; margin: 0;
    font-family: "Oswald", sans-serif; font-weight: 300; font-size: 46px; letter-spacing: 3px; color: var(--white);
  }
  .headline {
    position: absolute; left: 68px; right: 78px; margin: 0;
    font-family: "Oswald", sans-serif; font-weight: 600; color: var(--cream);
    line-height: 1; text-transform: uppercase;
  }
  .headline-1 { top: 178px; font-size: 196px; letter-spacing: 2px; }
  .headline-2 { top: 352px; font-size: 190px; text-align: right; letter-spacing: 4px; }
  .perk {
    position: absolute; left: 255px; right: 78px; top: 530px; height: 38px;
    background: var(--cream); color: var(--ink);
    display: flex; align-items: center; justify-content: center;
    font-weight: 900; font-size: 28px; letter-spacing: 14px;
  }
  .roles-label {
    position: absolute; right: 78px; top: 596px; height: 30px;
    display: flex; align-items: center; gap: 8px;
    font-weight: 700; font-size: 22px; letter-spacing: 3px;
  }
  .roles-label svg { display: block; }
  .roles {
    position: absolute; left: 85px; right: 78px; top: 640px; height: 322px;
    display: flex; gap: 18px;
  }
  .role { position: relative; flex: 1; overflow: hidden; }
  .role-photo { position: absolute; inset: 0; }
  .role-photo.printing { background: linear-gradient(160deg, #4a6f8e 0%, #9aa7b0 40%, #d85a3c 70%, #2d4c7a 100%); }
  .role-photo.construction { background: linear-gradient(160deg, #f1ede6 0%, #d9b98c 45%, #b88a55 75%, #6e5236 100%); }
  .role-en {
    position: absolute; left: 8px; top: 12px; writing-mode: vertical-rl;
    font-family: "Oswald", sans-serif; font-weight: 500; font-size: 40px; letter-spacing: 4px;
    color: rgba(255,255,255,0.7);
  }
  .role-tag {
    position: absolute; right: 12px; top: 14px; writing-mode: vertical-rl;
    padding: 8px 4px; border: 1.5px solid var(--ink); background: rgba(255,255,255,0.85);
    color: var(--ink); font-weight: 700; font-size: 15px; letter-spacing: 3px;
  }
  .company {
    position: absolute; left: 0; right: 0; top: 990px; margin: 0; text-align: center;
    font-weight: 500; font-size: 30px; letter-spacing: 2px;
  }
  .contact {
    position: absolute; left: 82px; right: 78px; top: 1040px;
    display: flex; align-items: center; justify-content: space-between;
  }
  .phone { display: flex; align-items: center; gap: 8px; font-family: "Oswald", sans-serif; font-weight: 500; font-size: 46px; letter-spacing: 1px; }
  .lines { display: flex; flex-direction: column; gap: 8px; font-size: 14px; color: var(--white); }
  .line { display: flex; align-items: center; gap: 8px; }
  .line.mail { font-size: 18px; }
  .line.url { font-size: 11px; color: var(--muted); }
</style>
</head>
<body>
<main class="poster">
  <div class="brand">
    <span class="brand-mark"></span>
    <span class="brand-name">MOKA</span>
  </div>

  <div class="watermark" aria-hidden="true">MOKA</div>

  <p class="lead">WE ARE LOOKING FOR</p>
  <h1 class="headline headline-1">CREATIVE</h1>
  <h1 class="headline headline-2">TARENTS</h1>

  <div class="perk">資格保有者優遇</div>

  <div class="roles-label">
    <svg width="34" height="24" viewBox="0 0 34 24"><polygon points="0,24 34,0 34,24" fill="#ffffff"/></svg>
    <span>募集職種</span>
  </div>

  <section class="roles">
    <article class="role">
      <div class="role-photo printing" role="img" aria-label="印刷機のローラーとカラー印刷物の写真"></div>
      <span class="role-en">PRINTING</span>
      <span class="role-tag">印刷事業</span>
    </article>
    <article class="role">
      <div class="role-photo construction" role="img" aria-label="木造住宅の骨組みの建設現場の写真"></div>
      <span class="role-en">CONSTRUCTION</span>
      <span class="role-tag">建設事業</span>
    </article>
  </section>

  <p class="company">株式会社森岡ホールディングス</p>

  <div class="contact">
    <div class="phone">
      <svg width="38" height="38" viewBox="0 0 24 24"><rect x="1" y="1" width="22" height="22" rx="3" fill="none" stroke="#fff" stroke-width="1.6"/><path d="M8 6l2 3-1.3 1.3a8 8 0 0 0 5 5L15 14l3 2-1 2.5c-5 0-10-5-10-10z" fill="#fff"/></svg>
      <span>086-431-5790</span>
    </div>
    <div class="lines">
      <div class="line mail">
        <svg width="18" height="14" viewBox="0 0 18 14"><rect x="1" y="1" width="16" height="12" fill="none" stroke="#fff" stroke-width="1.4"/><path d="M1 1l8 6 8-6" fill="none" stroke="#fff" stroke-width="1.4"/></svg>
        <span>moka2210@mokahd-mail.jp</span>
      </div>
      <div class="line url">
        <svg width="18" height="14" viewBox="0 0 18 14"><rect x="1" y="1" width="16" height="12" fill="none" stroke="#bdbdbd" stroke-width="1.4"/><line x1="1" y1="4" x2="17" y2="4" stroke="#bdbdbd" stroke-width="1.4"/></svg>
        <span>https://www.moka-holdings.jp/recruit.php</span>
      </div>
    </div>
  </div>
</main>
</body>
</html>
```